A new company focused on starting and investing in transformative businesses.

We need a simple and clean website with a few pages. we like larkmeadow.com as a starting point. we want the landing page to be very simple with an option to click through on the top right into INVESTOR LOGIN. then we want to be able to scroll down to see more about our company.

Target Market(s)

professional

Coding

Coded - Design and coding required

Number of Pages Required

2 page

Font styles to use
Serif
Sans Serif

Requirements
Must have
• HALVERN BUILDERS logo (attached as a file) on the top with INVESTOR LOGIN as a click through on the right. Please model the click through from larkmeadow.com. The description (also written in attached file) should be on the landing page. we do not want to have to scroll to read the description.

Then we can scroll down to read more about Halvern including the mission and the two types of businesses. More is detailed on the attached file called "Halvern Website Syntax"
Should not have
• should not be slow loading with lots of fancy graphics. should not be busy and with too many colors.

```html
<!DOCTYPE html>
<html lang="en">
<head>
<meta charset="utf-8">
<title>Halvern Builders</title>
<link rel="stylesheet" href="https://fonts.googleapis.com/css2?family=Montserrat:wght@300;400;500;600;700&family=Open+Sans:wght@400;600&display=swap">
<style>
  :root {
    --brand-blue: #0f5aa3;
    --ink: #231f20;
    --body-grey: #666666;
    --hero-grey: #e2e2e2;
    --footer-bg: #231f20;
    --footer-rule: #4a4647;
    --white: #ffffff;
  }
  * { margin: 0; padding: 0; box-sizing: border-box; }
  html, body { width: 1011px; height: 1200px; overflow: hidden; background: var(--white); }
  body { position: relative; font-family: "Open Sans", Arial, sans-serif; color: var(--ink); }

  .hero { position: absolute; left: 0; top: 0; width: 1011px; height: 536px; }
  .hero-panel {
    position: absolute; left: 0; top: 0; width: 474px; height: 536px;
    background: linear-gradient(180deg, #e6e6e6 0%, #dedede 70%, #d8dcdf 100%);
  }
  .brand { position: absolute; display: flex; align-items: center; gap: 12px; }
  .brand-mark { width: 22px; height: 22px; background: var(--brand-blue); }
  .brand-name {
    font-family: "Montserrat", Arial, sans-serif; font-weight: 600;
    font-size: 25px; line-height: 30px; letter-spacing: 0.5px; width: 160px;
  }
  .hero .brand { left: 94px; top: 22px; }
  .hero .brand-name { color: var(--ink); }

  .investor-login {
    position: absolute; right: 94px; top: 37px;
    display: flex; align-items: center; gap: 8px;
    font-family: "Montserrat", Arial, sans-serif; font-weight: 500;
    font-size: 16px; color: var(--ink); text-decoration: none; letter-spacing: 0.2px;
  }
  .investor-login svg { width: 12px; height: 14px; fill: var(--brand-blue); }

  .accent-bar { position: absolute; left: 94px; top: 178px; width: 117px; height: 4px; background: var(--brand-blue); }
  .hero-statement {
    position: absolute; left: 94px; top: 196px; width: 380px;
    font-family: "Montserrat", Arial, sans-serif; font-weight: 400;
    font-size: 28px; line-height: 41px; color: var(--ink);
  }
  .scroll-cue { position: absolute; left: 94px; top: 441px; width: 34px; height: 64px; }

  .hero-photo {
    position: absolute; left: 562px; top: 83px; width: 449px; height: 453px;
    background: linear-gradient(135deg, #b7c9d8 0%, #9fb3c4 35%, #c9b59a 60%, #5d6670 100%);
  }

  .about { position: absolute; left: 0; top: 536px; width: 1011px; height: 424px; }
  .mission {
    position: absolute; left: 94px; top: 62px; width: 330px;
    font-family: "Montserrat", Arial, sans-serif; font-weight: 400;
    font-size: 23px; line-height: 34.7px; color: var(--brand-blue);
  }
  .offering { position: absolute; left: 490px; width: 430px; }
  .offering-icon { position: absolute; left: 0; top: 0; width: 38px; height: 34px; fill: var(--brand-blue); }
  .offering-title {
    margin-left: 70px; font-family: "Montserrat", Arial, sans-serif; font-weight: 500;
    font-size: 21px; line-height: 26px; letter-spacing: 0.3px; color: var(--ink);
  }
  .offering-text {
    margin-left: 70px; margin-top: 10px; width: 360px;
    font-size: 14.6px; line-height: 24.5px; color: var(--body-grey);
  }
  .offering-ground { top: 64px; }
  .offering-special { top: 255px; }

  .site-footer { position: absolute; left: 0; top: 960px; width: 1011px; height: 240px; background: var(--footer-bg); color: var(--white); }
  .site-footer .brand { left: 94px; top: 28px; }
  .site-footer .brand-mark { background: var(--white); }
  .site-footer .brand-name { color: var(--white); }
  .media-note { position: absolute; left: 94px; top: 112px; font-size: 15.5px; line-height: 22px; }
  .media-email {
    position: absolute; left: 94px; top: 138px; display: flex; align-items: center; gap: 8px;
    font-size: 15.5px; font-weight: 600; color: var(--white); text-decoration: none;
  }
  .media-email svg { width: 15px; height: 12px; fill: var(--white); }
  .footer-rule { position: absolute; left: 94px; top: 186px; width: 823px; height: 1px; background: var(--footer-rule); }
  .copyright { position: absolute; left: 94px; top: 204px; font-size: 13px; line-height: 18px; }
</style>
</head>
<body>
  <header class="hero">
    <div class="hero-panel"></div>
    <div class="brand">
      <span class="brand-mark"></span>
      <span class="brand-name">HALVERN BUILDERS</span>
    </div>
    <a class="investor-login" href="#">
      <svg viewBox="0 0 12 14"><circle cx="6" cy="3.5" r="3.3"/><path d="M0 14c0-4 2.5-6.3 6-6.3s6 2.3 6 6.3z"/></svg>
      INVESTOR LOGIN
    </a>
    <div class="accent-bar"></div>
    <h1 class="hero-statement">Halvern Builders is an entrepreneurial firm focused on building and growing transformational companies</h1>
    <svg class="scroll-cue" viewBox="0 0 34 64" fill="none" stroke="#555" stroke-width="1.4">
      <rect x="1" y="1" width="30" height="50" rx="15"/>
      <circle cx="16" cy="13" r="3.5"/>
      <path d="M16 17v45M12 57l4 5 4-5"/>
    </svg>
    <div class="hero-photo" role="img" aria-label="Photo of a professional working on a laptop in a bright office"></div>
  </header>

  <main class="about">
    <p class="mission">Our mission is to build meaningful businesses that create enduring value by impacting people in a measurable way.</p>

    <section class="offering offering-ground">
      <svg class="offering-icon" viewBox="0 0 38 34">
        <path d="M0 0h2v32h36v2H0z"/>
        <rect x="7" y="20" width="4" height="10"/>
        <rect x="14" y="13" width="4" height="17"/>
        <rect x="21" y="17" width="4" height="13"/>
        <rect x="28" y="7" width="4" height="23"/>
      </svg>
      <h2 class="offering-title">GROUND UP</h2>
      <p class="offering-text">Our ground up business applies a proven analytic process to identify value edge, a form of competitive advantage. We architect transformational companies and are deliberate in creating the foundation necessary to lead an industry.</p>
    </section>

    <section class="offering offering-special">
      <svg class="offering-icon" viewBox="0 0 38 34">
        <circle cx="7" cy="6" r="4.5"/><circle cx="31" cy="6" r="4.5"/><circle cx="19" cy="10" r="6"/>
        <path d="M0 20c0-5 3-7 7-7 2 0 3.5.6 4.5 1.5-2 1.5-3 3.5-3 6.5H0z"/>
        <path d="M38 20c0-5-3-7-7-7-2 0-3.5.6-4.5 1.5 2 1.5 3 3.5 3 6.5H38z"/>
        <path d="M9 34v-8c0-6 4-9 10-9s10 3 10 9v8z"/>
      </svg>
      <h2 class="offering-title">SPECIAL OPPORTUNITIES</h2>
      <p class="offering-text">We partner with exceptional teams that create value by transforming lives. Our investment focus includes large companies and spin-outs.</p>
    </section>
  </main>

  <footer class="site-footer">
    <div class="brand">
      <span class="brand-mark"></span>
      <span class="brand-name">HALVERN BUILDERS</span>
    </div>
    <p class="media-note">For media inquiries, please contact</p>
    <a class="media-email" href="#">
      <svg viewBox="0 0 15 12"><path d="M0 0h15v1.5L7.5 6.5 0 1.5z"/><path d="M0 3.5l7.5 5 7.5-5V12H0z"/></svg>
      media@halvernbuilders.com
    </a>
    <div class="footer-rule"></div>
    <p class="copyright">Copyright © 2021, Halvern Builders.</p>
  </footer>
</body>
</html>
```